Web Design for company in the healthcare industry

We need a web design for a new company in the healthcare industry (telehealth) which allows patients to schedule appointments at their convenience, view and monitor their results, and consult with specialists that fit their requirements. The aim is to help patients take charge of their own health.

We already have a logo (attached) and are working with a developer who will do all the back end programming once the design is ready. Apart from the colours in the logo, we think shades of gray would work well.

Target Market(s)

I imagine the vast majority would be professionals from 30-50 years old.

Industry/Entity Type

Health And Wellness

Number of Pages Required

4 page

Requirements
Must have
• Hand-sketched graphics, particularly on landing page.
Should not have
• We don't want any photographs of people

```html
<!DOCTYPE html>
<html lang="en">
<head>
<meta charset="utf-8">
<title>Vitacare – Telehealth</title>
<link href="https://fonts.googleapis.com/css2?family=Open+Sans:wght@400;600;700&family=Lato:wght@300;400;700&display=swap" rel="stylesheet">
<style>
:root{
  --blue:#2b7bc4;
  --blue-dark:#1f5f9c;
  --green:#8cc63f;
  --green-dark:#76ad2f;
  --navy:#1c3a57;
  --navy-deep:#152d44;
  --gray-bg:#e9ebee;
  --gray-line:#d3d7dc;
  --text:#555b63;
  --text-light:#8a9099;
  --white:#ffffff;
}
*{box-sizing:border-box;margin:0;padding:0}
html,body{width:818px;height:1200px;overflow:hidden}
body{font-family:"Open Sans",Arial,sans-serif;color:var(--text);background:var(--white);position:relative;font-size:10px}
.abs{position:absolute}

/* header */
.topbar{top:0;right:18px;display:flex;gap:4px}
.topbar a{background:var(--navy);color:var(--white);font-size:7px;font-weight:700;padding:4px 8px;text-decoration:none;letter-spacing:.3px}
.topbar a.quote{background:var(--blue)}
.logo{top:30px;left:26px;display:flex;align-items:center;gap:6px;font-size:30px;font-weight:700;color:var(--blue);letter-spacing:-.5px}
.logo .dot{width:14px;height:14px;border-radius:50%;background:var(--green)}
.nav{top:30px;left:380px;display:flex}
.nav a{font-size:10px;color:var(--text);padding:8px 12px;text-decoration:none;font-weight:600}
.nav a.active{background:var(--green);color:var(--white)}
.dropdown{top:62px;left:442px;width:150px;background:var(--green);z-index:3;padding:4px 0}
.dropdown li{list-style:none;color:var(--white);font-size:9px;padding:5px 10px;border-bottom:1px solid rgba(255,255,255,.25);display:flex;align-items:center;gap:6px}
.dropdown li::before{content:"";width:5px;height:5px;background:var(--white)}

/* hero */
.hero{top:80px;left:0;width:818px;height:330px;background:linear-gradient(90deg,#e4e4e2 0%,#f4f4f2 45%,#fafaf8 100%)}
.hero-title{top:300px;left:462px;width:330px;font-family:Lato,sans-serif;font-weight:300;font-size:22px;line-height:1.28;color:#3a3f46}
.hero-band{top:410px;left:0;width:818px;height:20px;background:var(--white)}

/* content */
.content-bg{top:430px;left:0;width:818px;height:500px;background:var(--gray-bg)}
.card{background:var(--white);border:1px solid var(--gray-line);left:72px;width:486px}
.card h2{font-size:11px;font-weight:700;color:var(--blue);margin-bottom:5px;text-transform:uppercase}
.card p{font-size:8px;line-height:1.45;color:var(--text)}
.card .body{position:absolute;left:130px;top:14px;right:14px}
.icon{position:absolute;left:26px;top:18px;width:80px;height:80px}
.btn{display:inline-block;background:var(--blue);color:var(--white);font-size:8px;font-weight:700;padding:6px 10px;margin-top:8px;text-transform:uppercase}
.ticks{list-style:none;margin-top:4px}
.ticks li{font-size:8px;line-height:1.45;padding-left:12px;position:relative;margin-bottom:2px}
.ticks li::before{content:"✔";position:absolute;left:0;color:var(--green);font-size:8px}
.ticks b{color:var(--blue)}

.free h2{position:absolute;left:14px;top:12px}
.free .info{position:absolute;left:14px;top:34px;width:200px}
.free .info p{margin-bottom:8px}
.form{position:absolute;left:318px;top:30px;width:150px}
.form .field{height:17px;border:1px solid var(--gray-line);font-size:7px;color:var(--text-light);padding:3px 6px;margin-bottom:6px}

.sidebar{top:444px;left:568px;width:178px;background:var(--white);border:1px solid var(--gray-line)}
.sidebar h3{background:var(--blue);color:var(--white);font-size:8.5px;font-weight:700;padding:7px 8px;text-transform:uppercase}
.sidebar ul{list-style:none;padding:5px 8px}
.sidebar li{font-size:8px;line-height:17px;display:flex;align-items:center;gap:7px;color:var(--text)}
.sidebar li::before{content:"";width:7px;height:7px;border:1px solid #b8bec6}
.sidebar li.current{background:#f1f3f5;font-weight:700;color:var(--navy)}
.sidebar .see{display:block;margin:6px 8px 10px;background:var(--navy);color:var(--white);text-align:center;font-size:8px;font-weight:700;padding:6px}

/* testimonial */
.testi{top:930px;left:0;width:818px;height:150px;background:var(--white)}
.avatar{top:965px;left:240px;width:56px;height:56px;border-radius:50%;background:linear-gradient(#cfd6de,#aab4bf)}
.quote-mark{top:952px;left:308px;font-family:Lato,sans-serif;font-size:36px;color:var(--text-light)}
.quote-text{top:968px;left:312px;width:300px;font-size:8px;line-height:1.5}
.quote-name{top:1010px;left:312px;font-size:8.5px;font-weight:700;color:var(--navy)}
.quote-name span{font-weight:400;color:var(--text-light)}
.arrow{top:982px}

/* footer */
.footer{top:1084px;left:0;width:818px;height:116px;background:var(--navy)}
.fcol{top:1098px;color:#c7d3df}
.fcol h4{font-size:9px;font-weight:700;color:var(--white);margin-bottom:6px;display:flex;align-items:center;gap:5px}
.fcol h4::before{content:"";width:8px;height:8px;border-radius:50%;background:var(--green)}
.fcol li{list-style:none;font-size:7.5px;line-height:12px}
.fcol p{font-size:7.5px;line-height:1.5;width:170px}
.finput{height:16px;width:130px;background:var(--white);font-size:7px;color:var(--text-light);padding:3px 6px;margin-bottom:5px}
.fsubmit{display:inline-block;background:var(--blue);color:var(--white);font-size:7.5px;font-weight:700;padding:4px 12px}
.copy{top:1186px;left:0;width:818px;height:14px;background:var(--navy-deep);text-align:center;color:#9fb1c3;font-size:6.5px;line-height:14px}
</style>
</head>
<body>

<header>
  <div class="abs topbar"><a href="#">DOCUMENT ACTIVE</a><a href="#" class="quote">REQUEST A QUOTE</a></div>
  <div class="abs logo"><span>Vitacare</span><span class="dot"></span></div>
  <nav class="abs nav">
    <a href="#">Home</a><a href="#" class="active">Services</a><a href="#">Services</a><a href="#">Contact</a>
  </nav>
  <ul class="abs dropdown">
    <li>Nutritional Health</li><li>Weight Management</li><li>Women's Health</li>
    <li>Stress Management</li><li>Mens Health</li><li>Heart Disease</li>
  </ul>
</header>

<section>
  <div class="abs hero" role="img" aria-label="Hand-sketched pencil drawing of people doing yoga and stretching poses"></div>
  <h1 class="abs hero-title">Lorem Ipsum is simply dummy text of the printing and typesetting industry</h1>
  <div class="abs hero-band"></div>
</section>

<main>
  <div class="abs content-bg"></div>

  <article class="abs card" style="top:444px;height:122px">
    <svg class="icon" viewBox="0 0 80 80" aria-hidden="true">
      <circle cx="40" cy="40" r="36" fill="none" stroke="var(--gray-line)" stroke-width="2"/>
      <path d="M40 18 L58 25 V40 C58 52 49 60 40 63 C31 60 22 52 22 40 V25 Z" fill="var(--blue)"/>
      <path d="M40 50 C32 44 30 40 33 36 C35 33 39 34 40 37 C41 34 45 33 47 36 C50 40 48 44 40 50Z" fill="var(--white)"/>
    </svg>
    <div class="body">
      <h2>A Healthier You</h2>
      <p>Lorem ipsum dolor sit amet, consectetur adipiscing elit. Etiam accumsan, felis hendrerit convallis rutrum, convallis congue felis, vel elementum ligula justo vel turpis. Curabitur tempus nunc, tincidunt sed venenatis in, lobortis et ante. Lorem ipsum dolor sit amet, consectetur adipiscing.</p>
      <span class="btn">Get Details</span>
    </div>
  </article>

  <article class="abs card" style="top:578px;height:138px">
    <svg class="icon" viewBox="0 0 80 80" aria-hidden="true">
      <circle cx="40" cy="40" r="36" fill="none" stroke="var(--gray-line)" stroke-width="2"/>
      <rect x="20" y="22" width="40" height="36" rx="3" fill="var(--white)" stroke="#7d8590" stroke-width="2"/>
      <rect x="20" y="22" width="40" height="9" fill="#7d8590"/>
      <rect x="27" y="17" width="3" height="9" fill="#7d8590"/><rect x="50" y="17" width="3" height="9" fill="#7d8590"/>
      <g fill="#c2c8cf"><rect x="25" y="35" width="5" height="4"/><rect x="33" y="35" width="5" height="4"/><rect x="41" y="35" width="5" height="4"/><rect x="49" y="35" width="5" height="4"/><rect x="25" y="43" width="5" height="4"/><rect x="33" y="43" width="5" height="4"/><rect x="49" y="43" width="5" height="4"/></g>
      <rect x="41" y="43" width="5" height="4" fill="#e34b3c"/>
      <text x="40" y="72" text-anchor="middle" font-family="Open Sans,sans-serif" font-size="8" font-weight="700" fill="#e34b3c">Sep 24</text>
    </svg>
    <div class="body">
      <h2>Schedule an Appointment at Your Convenience</h2>
      <ul class="ticks">
        <li>Lorem ipsum dolor sit amet, consectetur adipiscing elit. Etiam accumsan, felis hendrerit convallis rutrum, convallis congue felis.</li>
        <li>Curabitur tempus nunc, tincidunt sed venenatis in, lobortis et ante. <b>Lorem ipsum dolor sit amet, consectetur adipiscing elit.</b></li>
      </ul>
      <span class="btn">Get Details</span>
    </div>
  </article>

  <article class="abs card free" style="top:730px;height:160px">
    <h2>Get a Free Appointment</h2>
    <div class="info">
      <p>Lorem ipsum is simply dummy text of the printing and typesetting industry. Lorem ipsum is simply dummy text of the printing and typesetting.</p>
      <p>Lorem ipsum is simply dummy text of the printing and typesetting industry. Lorem ipsum is simply dummy text of the printing and typesetting.</p>
    </div>
    <form class="form">
      <div class="field">Name</div>
      <div class="field">Email</div>
      <div class="field">Phone No</div>
      <span class="btn" style="margin-top:0">Appointment</span>
    </form>
  </article>

  <aside class="abs sidebar">
    <h3>Additional Health Packages</h3>
    <ul>
      <li>Allergy</li><li>Anti-Ageing Men</li><li>Anti-Ageing Women</li><li>Cardiovascular health</li>
      <li class="current">Diabetes</li><li>Food Intolerance</li><li>Heart Disease</li><li>Hormone Health</li>
      <li>Immunity</li><li>Liver Health</li><li>Mens Health</li><li>Nutritional Health</li>
      <li>Sports &amp; Performance</li><li>Stress &amp; Fatigue</li><li>Thyroid Health</li><li>Women's Health</li>
      <li>Weight Management</li>
    </ul>
    <span class="see">SEE ALL</span>
  </aside>
</main>

<section>
  <div class="abs testi"></div>
  <svg class="abs arrow" style="left:150px" width="14" height="24" viewBox="0 0 14 24" aria-hidden="true"><path d="M12 2 L2 12 L12 22" fill="none" stroke="#9aa2ab" stroke-width="2"/></svg>
  <svg class="abs arrow" style="left:654px" width="14" height="24" viewBox="0 0 14 24" aria-hidden="true"><path d="M2 2 L12 12 L2 22" fill="none" stroke="#9aa2ab" stroke-width="2"/></svg>
  <div class="abs avatar" role="img" aria-label="Portrait of the patient giving the testimonial"></div>
  <div class="abs quote-mark">“</div>
  <p class="abs quote-text">Lorem ipsum dolor sit amet, consectetur adipiscing elit. In porttitor tellus a sem tincidunt porta. Vestibulum sodales accumsan erat sed tempus. Sed velit orci, malesuada scelerisque risus id, feugiat laoreet diam. Nunc accumsan nisi.</p>
  <p class="abs quote-name">Jhon Deo <span>– Vice Client</span></p>
</section>

<footer>
  <div class="abs footer"></div>
  <div class="abs fcol" style="left:32px"><h4>Main Menu</h4><ul><li>Home</li><li>Services</li><li>Treatments</li><li>Contact Us</li></ul></div>
  <div class="abs fcol" style="left:200px"><h4>Useful Link</h4><ul><li>Terms &amp; Services</li><li>Accessible Site</li><li>Privacy</li><li>Site Map</li></ul></div>
  <div class="abs fcol" style="left:370px"><h4>About Us</h4><p>Lorem Ipsum is simply dummy text of the printing and typesetting industry. Lorem Ipsum has been the industry's standard dummy text ever since the 1500s, when an unknown printer took a galley.</p></div>
  <div class="abs fcol" style="left:638px"><h4>Get In Touch</h4><div class="finput">Your Name</div><div class="finput">Your Email Id</div><span class="fsubmit">SUBMIT</span></div>
  <div class="abs copy">© 2024 Vitacare. All rights reserved.</div>
</footer>

</body>
</html>
```